Business card & Stationary (e.g. Letterhead, Folder design, etc) for Financial Education Company
MoneyPathways
Creative Brief
Simple
Calder Pruitt
Founder & CEO
42 Hadley Ct, Ashford Glen, NJ 07099
calder@moneypathways.org
moneypathways.org
I would like to see a nice design, but I am leaving it up to you. It could be the company logo or name but with a nice design.

```html
<!DOCTYPE html>
<html lang="en">
<head>
<meta charset="utf-8">
<title>MoneyPathways Business Card</title>
<link href="https://fonts.googleapis.com/css2?family=Montserrat:wght@400;500;600;700&display=swap" rel="stylesheet">
<style>
  :root {
    --page-bg: #e6e6e6;
    --card-black: #0b0b0b;
    --card-white: #ffffff;
    --teal: #3fb0a6;
    --green: #3f9a3c;
    --ink: #1a1a1a;
    --muted: #666666;
    --grey-mark: #8a8a8a;
    --divider: #c8c8c8;
  }
  * { box-sizing: border-box; margin: 0; padding: 0; }
  html, body { width: 1200px; height: 901px; overflow: hidden; }
  body {
    background: var(--page-bg);
    font-family: "Montserrat", Arial, sans-serif;
    position: relative;
  }
  .card {
    position: absolute;
    left: 299px;
    width: 600px;
    height: 345px;
    border-radius: 18px;
    overflow: hidden;
  }
  .card-back { top: 70px; background: var(--card-black); }
  .card-front { top: 487px; background: var(--card-white); }

  .back-pattern {
    position: absolute;
    inset: 0;
    background: linear-gradient(90deg, rgba(255,255,255,0) 0%, rgba(255,255,255,0.03) 40%, rgba(255,255,255,0.14) 100%);
  }
  .back-brand {
    position: absolute;
    left: 0; right: 0; top: 148px;
    display: flex; align-items: center; justify-content: center; gap: 12px;
  }
  .back-brand .dot {
    width: 40px; height: 40px; border-radius: 50%;
    background: var(--grey-mark);
  }
  .back-brand .name {
    font-weight: 600; font-size: 34px; color: var(--grey-mark); letter-spacing: -0.5px;
  }

  .front-brand {
    position: absolute; left: 20px; top: 120px; width: 262px;
    display: flex; flex-direction: column; align-items: center; gap: 12px;
  }
  .front-brand .dot {
    width: 64px; height: 64px; border-radius: 50%; background: var(--teal);
  }
  .front-brand .name {
    font-weight: 600; font-size: 29px; color: var(--ink); letter-spacing: -0.5px;
  }
  .divider {
    position: absolute; left: 302px; top: 80px; width: 2px; height: 202px;
    background: var(--divider);
  }
  .details { position: absolute; left: 322px; top: 80px; }
  .person-name {
    font-size: 24px; font-weight: 500; letter-spacing: 0.5px; line-height: 1;
  }
  .person-name .first { color: var(--teal); }
  .person-name .last { color: var(--green); }
  .person-title { font-size: 12px; color: var(--muted); margin-top: 8px; }
  .address { font-size: 12px; color: var(--muted); margin-top: 18px; line-height: 17px; }
  .contacts { list-style: none; margin-top: 26px; }
  .contacts li {
    font-size: 12px; color: var(--muted); height: 23px;
    display: flex; align-items: center; gap: 8px;
  }
  .contacts svg { width: 11px; height: 11px; fill: var(--green); flex: none; }
  .wave { position: absolute; left: 0; bottom: 0; width: 600px; height: 90px; }
</style>
</head>
<body>
  <section class="card card-back" aria-label="Card back">
    <div class="back-pattern" role="img" aria-label="Faint repeated brand decoration"></div>
    <div class="back-brand">
      <span class="dot"></span>
      <span class="name">MoneyPathways</span>
    </div>
  </section>

  <section class="card card-front" aria-label="Card front">
    <div class="front-brand">
      <span class="dot"></span>
      <span class="name">MoneyPathways</span>
    </div>
    <div class="divider"></div>
    <div class="details">
      <h1 class="person-name"><span class="first">CALDER</span> <span class="last">PRUITT</span></h1>
      <p class="person-title">Founder &amp; CEO</p>
      <p class="address">42 Hadley Ct, Ashford Glen,<br>NJ 07099</p>
      <ul class="contacts">
        <li><svg viewBox="0 0 12 12"><path d="M2 1l2.5 0 1 3-1.5 1a7 7 0 0 0 3 3l1-1.5 3 1V10a1 1 0 0 1-1 1A9 9 0 0 1 1 2a1 1 0 0 1 1-1z"/></svg>555-014-2290</li>
        <li><svg viewBox="0 0 12 12"><rect x="0.5" y="2" width="11" height="8" rx="1"/></svg>calder@moneypathways.org</li>
        <li><svg viewBox="0 0 12 12"><circle cx="6" cy="6" r="5.5"/></svg>www.moneypathways.org</li>
      </ul>
    </div>
    <svg class="wave" viewBox="0 0 600 90" preserveAspectRatio="none" aria-hidden="true">
      <path d="M0 22 C120 -4 220 60 360 40 C460 26 540 12 600 30 L600 90 L0 90 Z" fill="var(--teal)"/>
      <path d="M0 34 C130 14 220 70 360 52 C460 40 540 26 600 40 L600 90 L0 90 Z" fill="var(--card-white)"/>
      <path d="M0 42 C130 24 220 80 360 62 C460 50 540 36 600 50 L600 90 L0 90 Z" fill="var(--card-black)"/>
    </svg>
  </section>
</body>
</html>
```